Design business card for startup company

Buildara is working on construction business and offering software as a service for construction companies helping their subcontracting process and making them easier and faster to sign legal contracts for different construction jobs. Now it is time to hit the markets and our company needs recognizable business cards. Business cards should include our company logo on backside(attached). Card design should be modern. Font used in logo is Montserrat-SemiBold.

Color codes of logo: #07599D (blue) & #616463 (Grey)

```html
<!DOCTYPE html>
<html lang="en">
<head>
<meta charset="utf-8">
<title>Buildara Business Card</title>
<link rel="stylesheet" href="https://fonts.googleapis.com/css2?family=Montserrat:wght@600&family=Roboto:wght@400;500;700&display=swap">
<style>
  :root {
    --brand-blue: #07599D;
    --brand-grey: #616463;
    --backdrop: #6a6a6a;
    --card-light: #e9e9e9;
    --card-light-edge: #e2e2e2;
    --text-white: #ffffff;
    --text-muted: #7a7c7b;
  }
  * { box-sizing: border-box; margin: 0; padding: 0; }
  html, body {
    width: 1200px;
    height: 1200px;
    overflow: hidden;
  }
  body {
    background: var(--backdrop);
    position: relative;
    font-family: "Roboto", Arial, sans-serif;
  }
  .card {
    position: absolute;
    left: 240px;
    width: 720px;
    height: 420px;
    border-radius: 16px;
    overflow: hidden;
  }
  .card-front {
    top: 140px;
    background: var(--brand-blue);
  }
  .card-back {
    top: 637px;
    background: linear-gradient(135deg, var(--card-light) 0%, var(--card-light-edge) 100%);
  }
  .wordmark {
    position: absolute;
    font-family: "Montserrat", Arial, sans-serif;
    font-weight: 600;
    text-transform: uppercase;
    white-space: nowrap;
    line-height: 1;
  }
  .card-front .wordmark {
    left: 0;
    right: 0;
    top: 186px;
    text-align: center;
    font-size: 46px;
    letter-spacing: 8px;
    color: var(--text-white);
  }
  .card-front .website {
    position: absolute;
    left: 0;
    right: 0;
    top: 362px;
    text-align: center;
    font-size: 18px;
    color: var(--text-white);
  }
  .card-back .wordmark {
    right: 40px;
    top: 42px;
    font-size: 30px;
    letter-spacing: 4px;
    color: var(--brand-blue);
  }
  .person-name {
    position: absolute;
    left: 38px;
    top: 237px;
    font-size: 29px;
    font-weight: 700;
    line-height: 1;
    color: var(--brand-grey);
  }
  .person-name .first { color: var(--brand-blue); }
  .person-role {
    position: absolute;
    left: 38px;
    top: 273px;
    font-size: 18px;
    color: var(--brand-grey);
  }
  .divider {
    position: absolute;
    left: 40px;
    top: 303px;
    width: 640px;
    height: 3px;
    background: var(--brand-blue);
  }
  .contact-list {
    position: absolute;
    left: 38px;
    top: 321px;
    list-style: none;
    font-size: 17.5px;
    line-height: 21px;
    color: var(--text-muted);
  }
  .contact-list .label {
    color: var(--brand-blue);
    font-weight: 500;
  }
  .address {
    position: absolute;
    left: 497px;
    top: 331px;
    font-style: normal;
    font-size: 16.5px;
    line-height: 21px;
    color: var(--text-muted);
  }
</style>
</head>
<body>
  <section class="card card-front">
    <div class="wordmark">Buildara</div>
    <div class="website">www.buildaraweb.com</div>
  </section>

  <section class="card card-back">
    <div class="wordmark">Buildara</div>
    <h1 class="person-name"><span class="first">DANIEL</span> REYES</h1>
    <p class="person-role">Founder &amp; Ceo</p>
    <div class="divider"></div>
    <ul class="contact-list">
      <li><span class="label">PHONE:</span> 000 48271 3590</li>
      <li><span class="label">EMAIL:</span> hello@buildaramail.com</li>
      <li><span class="label">WEBSITE:</span> www.buildaraweb.com</li>
    </ul>
    <address class="address">1475 Alder Ave, Suite 3B<br>Queens N.Y 11375</address>
  </section>
</body>
</html>
```